The Mariner’s Beacon – Leadership Transformation Infographic

I seek a high-quality, conceptual infographic.

🔹 Core Concept:
The model represents the shift from high-achiever to future-defining leader, moving from effort-based leadership to magnetic, presence-based influence. The vortex symbolizes continuous expansion, effortless influence, and infinite leadership mastery.

🔹 Key Visual Elements:
1️⃣ Sacred Gateway at the Core – Represents "A - Align with Power," the "dentity collapse & initiation into transformation.
2️⃣ Expanding Vortex Layers – Three main spiraling layers representing progressive shifts in leadership mastery:

Inner Spiral: Energy Shift
"L - Leverage Energy" (Stop chasing, start attracting)
"C - Collapse Time & Space" (Move beyond linear growth)
Mid Spiral: Influence Shift
"H - Harness Magnetic Presence" (Your presence shapes reality)
"E - Embody the Future Now" (Operate as your highest self today)
Outer Expansion: Legacy Shift
"M - Master Influence" (Move from persuasion to inevitability)
"Y - Yield Legacy" (Your leadership expands beyond you)

🔹 Design Aesthetic:
Ethereal, futuristic, and sacred—deep blues and gold to reflect transcendence, power, and flow.
Glowing energy lines to show leadership influence expanding naturally.
Typography must be modern, elegant, and straightforward.

🔹 Final Deliverable:
A high-resolution infographic that visually communicates the transformation process.
File formats: PNG, PDF, and editable AI/PSD files.
Looking forward to collaborating with a designer who understands sacred geometry, energy flow, and high-impact leadership visuals.

The uploaded rough sketch illustrates the envisioned energy and feel of the design. It serves as a guiding reference for the final execution and our style guide. The design will replace the seen graphic on the "product on a page" attached.

Target Market(s)

High-level executives, visionary founders, board members, and transformational leaders looking to move beyond high-achievement into effortless, presence-based leadership. This model is designed for those who operate at the highest levels of business, influence, and leadership impact.

Industry/Entity Type

Leadership, Personal Development, Executive Coaching, High-Performance Business Strategy, Visionary Growth, Legacy Building.

Font styles to use
Sans Serif
Other font styles liked:
• We use mainly LATO, as seen in the uploaded style guide

Requirements
Must have
• ✔ A powerful vortex design with a sacred gateway at the center, symbolizing initiation into leadership transformation. ✔ The P.R.I.S.T.O.N. framework elements must be clearly integrated into the visual structure. ✔ A futuristic, elegant, and high-impact feel—deep blues, golds, and ethereal glowing effects to represent transcendence and energy flow. ✔ Typography that is clear, modern, and elegant—no overly decorative or cartoonish fonts. ✔ A clean layout that ensures the transformation model is immediately understandable and visually compelling. // Merging the Best of Both Vortex Concepts (see attached images) Hi [Designer’s Name], I want to merge their strongest elements to create the perfect representation of he Summit Prism Horizon. 🔹 From Image 1 (Fire Vortex - V1): - The raw, explosive energy—this represents the ignition of transformation, the catalytic shift when a leader steps into their power. - The intensity and movement—it needs to feel alive, as if it’s actively pulling the viewer in. 🔹 From Image 2 (Galactic Vortex - V2): - The gravitational pull and infinite expansion—this embodies the legacy effect of leadership, showing that transformation doesn’t just happen once; it keeps unfolding. - The depth and magnetism—it should evoke a sense of stepping into something profound, a portal of infinite potential. 💡 The goal is to blend these two elements: The vortex should radiate power (Image 1) while also drawing people in with magnetic inevitability (Image 2). It’s not just about motion; it’s about feeling pulled into a transformational journey—a gateway to the highest level of leadership.
Nice to have
• ✨ Subtle sacred geometry elements woven into the design to reflect deep transformation and universal flow. ✨ A gradient effect that enhances the energy and depth of the vortex. ✨ Faint cosmic or nebula-inspired background effects to enhance the sense of infinite expansion. ✨ Minimalist yet dynamic motion effect (if applicable) to give it a sense of movement and flow.
Should not have
• 🚫 No generic “business” graphics or corporate-style visuals—this is NOT a traditional leadership model. 🚫 No overused stock imagery—this must feel custom, unique, and premium. 🚫 No harsh, dark, or aggressive colors—this is about power through presence, not force. 🚫 No clutter—everything must feel intentional, spacious, and elegantly structured.

```html
<!DOCTYPE html>
<html lang="en">
<head>
<meta charset="UTF-8">
<title>Leadership Transformation Vortex</title>
<link rel="stylesheet" href="https://fonts.googleapis.com/css2?family=Lato:wght@400;700;900&display=swap">
<style>
  :root {
    --space: #07050c;
    --deep-purple: #3a0f45;
    --plum: #5e1a66;
    --magenta: #c23fb2;
    --orange: #f08a2a;
    --amber: #b8561c;
    --gold-light: #f6d7b0;
    --mist: #dde9ef;
    --cyan: #37c0ea;
    --core: #7fe0ff;
    --label: #ffffff;
    --core-label: #000000;
  }
  html, body {
    margin: 0;
    padding: 0;
    width: 1200px;
    height: 933px;
    overflow: hidden;
    background: var(--space);
  }
  .infographic {
    position: relative;
    width: 1200px;
    height: 933px;
    overflow: hidden;
  }
  .vortex-art {
    position: absolute;
    inset: 0;
  }
  .vortex-art__nebula,
  .vortex-art__arms,
  .vortex-art__inner,
  .vortex-art__core {
    position: absolute;
    inset: 0;
  }
  .vortex-art__nebula {
    background:
      radial-gradient(ellipse 58% 66% at 52% 52%,
        var(--magenta) 0%,
        var(--plum) 45%,
        var(--deep-purple) 68%,
        var(--space) 100%);
  }
  .vortex-art__arms {
    background:
      conic-gradient(from 20deg at 52% 50%,
        var(--orange) 0deg,
        var(--gold-light) 40deg,
        var(--amber) 80deg,
        var(--magenta) 120deg,
        var(--plum) 160deg,
        var(--orange) 200deg,
        var(--gold-light) 235deg,
        var(--amber) 270deg,
        var(--magenta) 310deg,
        var(--orange) 360deg);
    -webkit-mask-image: radial-gradient(ellipse 40% 48% at 52% 50%, #000 40%, rgba(0,0,0,0.6) 70%, transparent 100%);
            mask-image: radial-gradient(ellipse 40% 48% at 52% 50%, #000 40%, rgba(0,0,0,0.6) 70%, transparent 100%);
    filter: blur(18px);
  }
  .vortex-art__inner {
    background:
      conic-gradient(from 200deg at 51% 50%,
        var(--mist) 0deg,
        var(--cyan) 70deg,
        var(--mist) 140deg,
        #7a6a6a 190deg,
        var(--cyan) 250deg,
        var(--mist) 310deg,
        var(--mist) 360deg);
    -webkit-mask-image: radial-gradient(ellipse 19% 25% at 51% 50%, #000 55%, transparent 100%);
            mask-image: radial-gradient(ellipse 19% 25% at 51% 50%, #000 55%, transparent 100%);
    filter: blur(10px);
  }
  .vortex-art__core {
    background: radial-gradient(ellipse 9% 12% at 50% 50%, #e6fbff 0%, var(--core) 40%, rgba(55,192,234,0) 100%);
  }
  .labels {
    position: absolute;
    inset: 0;
    width: 1200px;
    height: 933px;
    font-family: 'Lato', sans-serif;
  }
  .step-title {
    fill: var(--label);
    font-weight: 700;
    font-size: 22px;
    letter-spacing: 1.5px;
    paint-order: stroke;
    stroke: rgba(0,0,0,0.3);
    stroke-width: 2px;
  }
  .step-title--outer { font-size: 23px; }
  .step-note {
    fill: var(--label);
    font-weight: 400;
    font-size: 9.5px;
    letter-spacing: 1.2px;
  }
  .core-title {
    fill: var(--core-label);
    font-weight: 900;
    font-size: 33px;
    text-anchor: middle;
  }
</style>
</head>
<body>
<main class="infographic">
  <div class="vortex-art" role="img" aria-label="Glowing cosmic vortex spiralling inward from purple and magenta nebula through orange and gold arms to a bright blue core, set in deep space">
    <div class="vortex-art__nebula"></div>
    <div class="vortex-art__arms"></div>
    <div class="vortex-art__inner"></div>
    <div class="vortex-art__core"></div>
  </div>

  <svg class="labels" viewBox="0 0 1200 933" xmlns="http://www.w3.org/2000/svg">
    <defs>
      <path id="path-collapse" d="M 512 352 Q 640 265 800 378 L 830 400"/>
      <path id="path-collapse-note" d="M 527 368 Q 622 305 726 360 L 750 375"/>
      <path id="path-leverage" d="M 572 620 Q 690 600 727 480 L 735 450"/>
      <path id="path-leverage-note" d="M 569 631 Q 695 635 744 540 L 755 515"/>
      <path id="path-harness" d="M 372 472 C 365 340 400 220 530 140 L 560 122"/>
      <path id="path-harness-note" d="M 400 472 Q 392 330 437 238 L 448 215"/>
      <path id="path-embody" d="M 311 644 Q 414 731 620 720 L 650 718"/>
      <path id="path-embody-note" d="M 304 663 Q 393 737 538 746 L 565 747"/>
      <path id="path-master" d="M 998 427 Q 1070 516 1092 655 L 1097 690"/>
      <path id="path-master-note" d="M 984 434 Q 1040 538 1069 690 L 1074 720"/>
      <path id="path-yield" d="M 137 378 Q 140 280 165 200 L 175 170"/>
      <path id="path-yield-note" d="M 170 398 Q 170 259 227 140 L 240 115"/>
    </defs>

    <g class="core">
      <text class="core-title" x="599" y="448">ALIGN</text>
      <text class="core-title" x="599" y="478">WITH</text>
      <text class="core-title" x="599" y="508">POWER</text>
    </g>

    <g class="step step--collapse">
      <text class="step-title" textLength="310" lengthAdjust="spacingAndGlyphs"><textPath href="#path-collapse">COLLAPSE TIME &amp; SPACE</textPath></text>
      <text class="step-note" textLength="205" lengthAdjust="spacingAndGlyphs"><textPath href="#path-collapse-note">MOVE BEYOND LINEAR GROWTH</textPath></text>
    </g>

    <g class="step step--leverage">
      <text class="step-title" textLength="212" lengthAdjust="spacingAndGlyphs"><textPath href="#path-leverage">LEVERAGE ENERGY</textPath></text>
      <text class="step-note" textLength="195" lengthAdjust="spacingAndGlyphs"><textPath href="#path-leverage-note">STOP CHASING, START ATTRACTING</textPath></text>
    </g>

    <g class="step step--harness">
      <text class="step-title step-title--outer" textLength="378" lengthAdjust="spacingAndGlyphs"><textPath href="#path-harness">HARNESS MAGNETIC PRESENCE</textPath></text>
      <text class="step-note" textLength="235" lengthAdjust="spacingAndGlyphs"><textPath href="#path-harness-note">YOUR PRESENCE SHAPES REALITY</textPath></text>
    </g>

    <g class="step step--embody">
      <text class="step-title" textLength="315" lengthAdjust="spacingAndGlyphs"><textPath href="#path-embody">EMBODY THE FUTURE NOW</textPath></text>
      <text class="step-note" textLength="248" lengthAdjust="spacingAndGlyphs"><textPath href="#path-embody-note">OPERATE AS YOUR HIGHEST SELF TODAY</textPath></text>
    </g>

    <g class="step step--master">
      <text class="step-title step-title--outer" textLength="236" lengthAdjust="spacingAndGlyphs"><textPath href="#path-master">MASTER INFLUENCE</textPath></text>
      <text class="step-note" textLength="265" lengthAdjust="spacingAndGlyphs"><textPath href="#path-master-note">MOVE FROM PERSUASION TO INEVITABILITY</textPath></text>
    </g>

    <g class="step step--yield">
      <text class="step-title step-title--outer" textLength="175" lengthAdjust="spacingAndGlyphs"><textPath href="#path-yield">YIELD LEGACY</textPath></text>
      <text class="step-note" textLength="252" lengthAdjust="spacingAndGlyphs"><textPath href="#path-yield-note">YOUR LEADERSHIP EXPANDS BEYOND</textPath></text>
    </g>
  </svg>
</main>
</body>
</html>
```